Business card, letterhead, envelope design, email footer for non-profit private equity association
Riviera Growth Capital and Seed Funding Society
Business card, letterhead, envelope design, email footer for non-profit private equity association - Financial Services
Creative Brief
Simple
Tobias Hernquist
Head of Operations
17, Rue des Orangers 98000 Monaco
thernquist@rgsf-example.org
www.rgsf-example.org
Stationery will be prepared for all 7-8 Board Members of our non-profit association. The stationery design is a subsequent process of the new logo design, which has just been created. The Riviera Growth Capital & Seed Funding Society (RGSF) stands for: seriousness and professionalism. Our official website is http://www.rgsf-example.org Please note that this website still includes the OLD logo and layout (to be changed shortly, so please do not let that influence you. This is more to show you the content rather than the design.

```html
<!DOCTYPE html>
<html lang="en">
<head>
<meta charset="utf-8">
<title>Riviera Growth Capital &amp; Seed Funding Society — Business Card</title>
<link href="https://fonts.googleapis.com/css2?family=Montserrat:wght@400;500;600;700&display=swap" rel="stylesheet">
<style>
  :root {
    --backdrop: #e4e5e7;
    --card: #ffffff;
    --ink: #2f2f33;
    --ink-soft: #5a5a60;
    --accent: #d2232a;
    --band: #2b2b2e;
    --shadow: rgba(0,0,0,0.16);
  }
  html, body {
    margin: 0;
    padding: 0;
    width: 1200px;
    height: 883px;
    overflow: hidden;
    background: var(--backdrop);
    font-family: "Montserrat", Arial, sans-serif;
    color: var(--ink);
  }
  .canvas {
    position: relative;
    width: 1200px;
    height: 883px;
  }
  .card {
    position: absolute;
    width: 580px;
    height: 330px;
    background: var(--card);
    border-radius: 30px;
    box-shadow: 0 14px 34px var(--shadow);
    overflow: hidden;
  }
  .card--back { left: 560px; top: 90px; }
  .card--front { left: 80px; top: 440px; }

  .brand {
    position: absolute;
    display: flex;
    flex-direction: column;
  }
  .brand__row {
    display: flex;
    align-items: center;
    gap: 12px;
  }
  .brand__dot {
    width: 16px;
    height: 16px;
    border-radius: 50%;
    background: var(--accent);
  }
  .brand__name {
    font-weight: 700;
    font-size: 54px;
    letter-spacing: 2px;
    line-height: 1;
    color: var(--ink);
  }
  .brand__full {
    margin-top: 8px;
    font-weight: 500;
    font-size: 12.5px;
    letter-spacing: 0.6px;
    line-height: 1.3;
    text-transform: uppercase;
    color: var(--ink);
    max-width: 290px;
  }
  .card--back .brand { left: 150px; top: 110px; }
  .card--front .brand { right: 50px; top: 48px; }

  .tab {
    position: absolute;
    left: 0;
    top: 120px;
    width: 14px;
    height: 56px;
    background: var(--band);
    border-radius: 0 6px 6px 0;
  }
  .holder {
    position: absolute;
    left: 38px;
    top: 126px;
  }
  .holder__name {
    font-weight: 600;
    font-size: 15px;
    text-transform: uppercase;
    color: var(--accent);
    letter-spacing: 0.4px;
  }
  .holder__title {
    margin-top: 3px;
    font-size: 12px;
    color: var(--ink-soft);
  }
  .contacts {
    position: absolute;
    left: 38px;
    top: 186px;
    list-style: none;
    margin: 0;
    padding: 0;
    font-size: 11px;
    color: var(--ink-soft);
  }
  .contacts li {
    display: flex;
    align-items: center;
    gap: 8px;
    height: 19px;
  }
  .contacts svg { width: 11px; height: 11px; fill: var(--accent); }
  .address {
    position: absolute;
    right: 50px;
    top: 196px;
    font-size: 11px;
    line-height: 1.5;
    color: var(--ink-soft);
    text-align: left;
  }
  .band {
    position: absolute;
    left: 0;
    right: 0;
    bottom: 0;
    height: 30px;
    background: var(--band);
  }
</style>
</head>
<body>
<main class="canvas">

  <section class="card card--back" aria-label="Business card, back">
    <div class="brand">
      <div class="brand__row">
        <span class="brand__name">RGSF</span>
        <span class="brand__dot"></span>
      </div>
      <span class="brand__full">Riviera Growth Capital and Seed Funding Society</span>
    </div>
  </section>

  <section class="card card--front" aria-label="Business card, front">
    <div class="brand">
      <div class="brand__row">
        <span class="brand__name">RGSF</span>
        <span class="brand__dot"></span>
      </div>
      <span class="brand__full">Riviera Growth Capital and Seed Funding Society</span>
    </div>

    <span class="tab"></span>
    <div class="holder">
      <div class="holder__name">Tobias Hernquist</div>
      <div class="holder__title">Managing Director</div>
    </div>

    <ul class="contacts">
      <li>
        <svg viewBox="0 0 24 24"><path d="M6.6 10.8a15.1 15.1 0 0 0 6.6 6.6l2.2-2.2c.3-.3.7-.4 1-.2 1.1.4 2.3.6 3.6.6.6 0 1 .4 1 1V20c0 .6-.4 1-1 1C10.6 21 3 13.4 3 4c0-.6.4-1 1-1h3.5c.6 0 1 .4 1 1 0 1.3.2 2.5.6 3.6.1.3 0 .7-.2 1z"/></svg>
        <span>+377 93 00 01 10</span>
      </li>
      <li>
        <svg viewBox="0 0 24 24"><path d="M7 2h10a2 2 0 0 1 2 2v16a2 2 0 0 1-2 2H7a2 2 0 0 1-2-2V4a2 2 0 0 1 2-2zm0 3v13h10V5z"/></svg>
        <span>+377 60 00 01 11</span>
      </li>
      <li>
        <svg viewBox="0 0 24 24"><path d="M6 3h12v5H6zM4 9h16a2 2 0 0 1 2 2v6h-4v4H6v-4H2v-6a2 2 0 0 1 2-2zm4 7v3h8v-3z"/></svg>
        <span>+377 93 00 01 12</span>
      </li>
      <li>
        <svg viewBox="0 0 24 24"><path d="M2 5h20v14H2zm2 2v.5l8 5 8-5V7zm0 3v7h16v-7l-8 5z"/></svg>
        <span>thernquist@rgsf-example.org</span>
      </li>
      <li>
        <svg viewBox="0 0 24 24"><path d="M12 2a10 10 0 1 0 0 20 10 10 0 0 0 0-20zm1 17.9V17h-2v2.9A8 8 0 0 1 4.1 13H7v-2H4.1A8 8 0 0 1 11 4.1V7h2V4.1a8 8 0 0 1 6.9 6.9H17v2h2.9a8 8 0 0 1-6.9 6.9z"/></svg>
        <span>www.rgsf-example.org</span>
      </li>
    </ul>

    <address class="address" style="font-style: normal;">
      17, Rue des Orangers<br>98000 Monaco
    </address>

    <span class="band"></span>
  </section>

</main>
</body>
</html>
```